Local fast-growing company in the service sector

We are looking for a modern business card design, which should also appear on our letterheads

Target Market(s)

Private and industrial sectors

Contact Information for Business Card

Vorname Name
Lindkofer Str. 18
71468 Ostheldern
Tel.: 07163-418259-0
Name@kovaltec-pbz.de

Colors
9d9d9d
919191
aaaaaa

Requirements
Must have
• The logo (file) in silver

```html
<!DOCTYPE html>
<html lang="de">
<head>
<meta charset="utf-8">
<title>Kovaltec – Visitenkarte</title>
<link rel="stylesheet" href="https://fonts.googleapis.com/css2?family=Source+Sans+3:wght@400;600;700&display=swap">
<style>
  :root {
    --stage: #000000;
    --card-dark: #3a3b3f;
    --card-dark-edge: #333438;
    --card-light: #ffffff;
    --silver: #9d9d9d;
    --silver-mid: #919191;
    --silver-light: #aaaaaa;
    --name-grey: #8c8c8e;
    --text-light: #e4e4e4;
    --divider: #2c2d30;
  }
  * { margin: 0; padding: 0; box-sizing: border-box; }
  html, body {
    width: 1200px; height: 900px; overflow: hidden;
    background: var(--stage);
    font-family: "Source Sans 3", "Myriad Pro", sans-serif;
  }
  .stage { position: relative; width: 1200px; height: 900px; }
  .card {
    position: absolute; top: 271px;
    width: 457px; height: 281px; border-radius: 14px;
  }
  .card--front {
    left: 137px;
    background: linear-gradient(180deg, var(--card-dark) 0%, var(--card-dark-edge) 100%);
  }
  .card--back { left: 626px; background: var(--card-light); }

  .brand-mark {
    position: absolute; left: 58px; top: 118px;
    width: 150px; text-align: center;
    font-size: 27px; font-weight: 700; letter-spacing: 1px;
    color: var(--silver);
  }
  .divider {
    position: absolute; left: 231px; top: 78px;
    width: 1px; height: 120px; background: var(--divider);
  }
  .contact { position: absolute; left: 258px; top: 76px; color: var(--text-light); }
  .contact__name {
    font-size: 17px; font-weight: 600; color: var(--name-grey);
    margin-bottom: 12px;
  }
  .contact__address { font-size: 13px; line-height: 17px; margin-bottom: 17px; }
  .contact__list { list-style: none; font-size: 13px; line-height: 16.5px; }
  .contact__list li { display: flex; align-items: center; }
  .contact__list svg { width: 9px; height: 9px; margin-right: 7px; fill: var(--silver-mid); }

  .logo {
    position: absolute; left: 0; right: 0; top: 108px;
    display: flex; align-items: center; justify-content: center; gap: 18px;
  }
  .logo__square { width: 58px; height: 58px; background: var(--silver-light); border-radius: 3px; }
  .logo__name {
    font-size: 52px; font-weight: 700; letter-spacing: 1px;
    color: var(--silver); line-height: 1;
  }
</style>
</head>
<body>
<main class="stage">
  <section class="card card--front" aria-label="Vorderseite">
    <div class="brand-mark">KOVALTEC</div>
    <div class="divider"></div>
    <div class="contact">
      <p class="contact__name">Vorname Name</p>
      <p class="contact__address">Lindkofer Str. 18<br>71468 Ostheldern</p>
      <ul class="contact__list">
        <li><svg viewBox="0 0 10 10" aria-hidden="true"><path d="M2 0.5 L3.8 2.6 L2.9 3.8 C3.6 5.2 4.8 6.4 6.2 7.1 L7.4 6.2 L9.5 8 L8.3 9.5 C4.3 9 1 5.7 0.5 1.7 Z"/></svg>07163-418259-0</li>
        <li><svg viewBox="0 0 10 10" aria-hidden="true"><path d="M0.5 2 H9.5 V8.5 H0.5 Z M1 2.3 L5 5.4 L9 2.3 V3 L5 6.2 L1 3 Z" fill-rule="evenodd"/></svg>Name@kovaltec-pbz.de</li>
        <li><svg viewBox="0 0 10 10" aria-hidden="true"><circle cx="5" cy="5" r="4.5"/></svg>www.kovaltec-pbz.de</li>
      </ul>
    </div>
  </section>

  <section class="card card--back" aria-label="Rückseite">
    <div class="logo">
      <span class="logo__square"></span>
      <span class="logo__name">KOVALTEC</span>
    </div>
  </section>
</main>
</body>
</html>
```